Marisol business card and stationary
business card and stationary
Marisol business card and stationary - Retailers
Creative Brief
Bright & Fun-filled
Janet Wroblenko
owner, designer
marisol a florist 418 north brook lane greenville, sc 29174
info@marisolblooms.example
marisolblooms.example
Concepts
Stationery for Online Retailer

```html
<!DOCTYPE html>
<html lang="en">
<head>
<meta charset="utf-8">
<title>Marisol Stationery</title>
<link href="https://fonts.googleapis.com/css2?family=Quicksand:wght@400;600;700&display=swap" rel="stylesheet">
<style>
  :root {
    --backdrop: #ebe6de;
    --paper: #ffffff;
    --pink: #e8798c;
    --pink-soft: #f7c9cf;
    --pink-pale: #fde9e6;
    --cream: #fff6dc;
    --ink: #6e6a6b;
    --ink-light: #9a9596;
    --petal: #eeeeee;
    --edge: #d8d4d0;
  }
  * { box-sizing: border-box; margin: 0; padding: 0; }
  html, body { width: 1200px; height: 1035px; overflow: hidden; }
  body {
    position: relative;
    background: var(--backdrop);
    font-family: "Quicksand", sans-serif;
    color: var(--ink);
  }
  .sheet {
    position: absolute;
    background: var(--paper);
    box-shadow: 0 2px 6px rgba(0,0,0,.18);
    overflow: hidden;
  }
  .petal-art {
    position: absolute;
    border-radius: 50%;
    background: radial-gradient(circle, #fafafa 0%, var(--petal) 45%, rgba(238,238,238,0) 72%);
  }
  .brand {
    position: absolute;
    display: flex;
    align-items: center;
    gap: 8px;
    white-space: nowrap;
  }
  .brand-dot {
    width: 30px; height: 30px;
    border-radius: 50%;
    background: var(--pink);
    flex: none;
  }
  .brand-name {
    font-weight: 700;
    color: var(--ink);
    line-height: 1;
  }
  .contact {
    position: absolute;
    font-size: 9px;
    line-height: 1.45;
    color: var(--ink-light);
    white-space: nowrap;
  }

  /* business cards */
  .card { top: 34px; width: 118px; height: 210px; border-radius: 4px; }
  .card-front { left: 107px; background: radial-gradient(circle at 50% 50%, var(--cream) 0%, var(--pink-pale) 45%, var(--pink-soft) 100%); }
  .card-plain { left: 244px; }
  .card-info { left: 384px; }
  .card .brand { left: 50%; top: 50%; transform: translate(-50%,-50%); }
  .card .brand-dot { width: 18px; height: 18px; }
  .card .brand-name { font-size: 20px; }
  .card-bloom {
    position: absolute; left: -20px; top: -10px; width: 90px; height: 230px;
    background: radial-gradient(ellipse at 30% 50%, var(--pink-soft) 0%, #fbe0e3 55%, rgba(255,255,255,0) 80%);
  }
  .card-person { position: absolute; right: 8px; top: 14px; text-align: right; }
  .card-person .name { font-size: 10px; font-weight: 700; color: var(--pink); }
  .card-person .role { font-size: 7px; color: var(--ink-light); }
  .card-info .contact { right: 8px; top: 70px; text-align: right; font-size: 6.5px; }

  /* letterhead */
  .letterhead { left: 50px; top: 266px; width: 530px; height: 715px; }
  .letterhead .petal-art { right: -110px; top: -150px; width: 420px; height: 420px; }
  .letterhead .brand { left: 28px; top: 72px; }
  .letterhead .brand-dot { width: 26px; height: 26px; }
  .letterhead .brand-name { font-size: 28px; }
  .letterhead .contact { left: 250px; top: 60px; font-size: 8.5px; }

  /* envelopes */
  .envelope-large { left: 597px; top: 90px; width: 544px; height: 470px; }
  .envelope-large .petal-art { right: -80px; bottom: -60px; width: 520px; height: 520px; }
  .envelope-large .brand-top { right: 120px; top: 18px; }
  .envelope-large .brand-top .brand-name { font-size: 15px; }
  .envelope-large .brand-top .brand-dot { width: 14px; height: 14px; }
  .envelope-large .brand-main { left: 18px; top: 185px; }
  .envelope-large .brand-main .brand-name { font-size: 24px; }
  .envelope-large .contact { left: 30px; top: 224px; font-size: 7.5px; }

  .envelope-flap { left: 597px; top: 589px; width: 544px; height: 126px; }
  .envelope-flap svg { position: absolute; inset: 0; }
  .envelope-flap .petal-art { right: -40px; top: -90px; width: 280px; height: 280px; }
  .envelope-flap .brand { left: 232px; top: 36px; }
  .envelope-flap .brand-name { font-size: 15px; }
  .envelope-flap .brand-dot { width: 14px; height: 14px; }

  .envelope-business { left: 597px; top: 735px; width: 544px; height: 252px; }
  .envelope-business .petal-art { right: -40px; top: -130px; width: 420px; height: 420px; }
  .envelope-business .brand { left: 18px; top: 30px; }
  .envelope-business .brand-name { font-size: 26px; }
  .envelope-business .contact { left: 28px; top: 80px; font-size: 7.5px; }
</style>
</head>
<body>

  <section class="sheet card card-front">
    <div class="brand"><span class="brand-dot"></span><span class="brand-name">marisol</span></div>
  </section>

  <section class="sheet card card-plain">
    <div class="brand"><span class="brand-dot"></span><span class="brand-name">marisol</span></div>
  </section>

  <section class="sheet card card-info">
    <div class="card-bloom" role="img" aria-label="Soft pink dahlia flower illustration"></div>
    <div class="card-person">
      <div class="name">Janet Wroblenko</div>
      <div class="role">owner, designer</div>
    </div>
    <div class="contact">
      marisol a florist<br>
      418 north brook lane<br>
      greenville, sc 29174<br><br>
      864.555.0142<br>
      info@marisolblooms.example<br>
      marisolblooms.example
    </div>
  </section>

  <section class="sheet letterhead">
    <div class="petal-art" role="img" aria-label="Large faint white dahlia petals decoration"></div>
    <div class="brand"><span class="brand-dot"></span><span class="brand-name">marisol</span></div>
    <div class="contact">
      marisol a florist<br>
      418 north brook lane<br>
      greenville, sc 29174<br><br>
      864.555.0142<br>
      info@marisolblooms.example<br>
      marisolblooms.example
    </div>
  </section>

  <section class="sheet envelope-large">
    <div class="petal-art" role="img" aria-label="Large faint white dahlia petals decoration"></div>
    <div class="brand brand-top"><span class="brand-dot"></span><span class="brand-name">marisol</span></div>
    <div class="brand brand-main"><span class="brand-dot"></span><span class="brand-name">marisol</span></div>
    <div class="contact">
      marisol a florist<br>
      418 north brook lane<br>
      greenville, sc 29174
    </div>
  </section>

  <section class="sheet envelope-flap">
    <div class="petal-art" role="img" aria-label="Faint white dahlia petals decoration"></div>
    <svg width="544" height="126" viewBox="0 0 544 126" aria-hidden="true">
      <polyline points="0,6 30,60 514,60 544,6" fill="none" stroke="var(--edge)" stroke-width="1"/>
    </svg>
    <div class="brand"><span class="brand-dot"></span><span class="brand-name">marisol</span></div>
  </section>

  <section class="sheet envelope-business">
    <div class="petal-art" role="img" aria-label="Large faint white dahlia petals decoration"></div>
    <div class="brand"><span class="brand-dot"></span><span class="brand-name">marisol</span></div>
    <div class="contact">
      marisol a florist<br>
      418 north brook lane<br>
      greenville, sc 29174
    </div>
  </section>

</body>
</html>
```